COVID-19 Related Signage for Hotel

Need to create new COVID-19 related signage utilizing our brand assets. Please use screenshots for copy/direction. essentially duplicate the screenshots but with our logo/branding.

All brand assets have been uploaded and examples of signage content. Pictures are not necessary but you can add them if you want similar to the examples attached.

Sign requirements

sign 1. Text "Hand Sanitizer Station" can add graphic
sign 2. Text "Protect Yourself" duplicate copy in the attached pictures
sign 3. Text "Face Mask Required" can add graphic
sign 4. Text "Face Covering Do's and Don'ts with text from "Face-covering checklist.jpg" REMOVE BWT logo or website or 3 face mask graphics
sign 5. Text "Maintain 6 Foot Distance" This sign will be printed and placed on the ground for guests to know where to stand in queue. Would prefer a circular Design. sign 6. Text "Wet, Lather, Scrub, Rinse, Dry" similar to screenshots attached.

ALL signs should have same look and feel throughout utilizing our brand graphics, logo, colors, and guidelines.

Target Market(s)

Hotel Guests

Industry/Entity Type

Hotel

Font styles to use
Sans Serif

Requirements
Must have
• Cohesive, unified branding look and feel

Should not have
• any use of the word "COVID-19" or Coronavirus.

```html
<!DOCTYPE html>
<html lang="en">
<head>
<meta charset="utf-8">
<title>Hand Sanitizer Station Signs</title>
<link href="https://fonts.googleapis.com/css2?family=Oswald:wght@400;700&display=swap" rel="stylesheet">
<style>
  :root {
    --backdrop: #5e5264;
    --brand-teal: #00aeb8;
    --brand-orange: #ff7f0f;
    --sign-white: #ffffff;
    --bottle-light: #d9f1f4;
    --bottle-mid: #4fc0c9;
  }
  html, body {
    margin: 0;
    padding: 0;
    overflow: hidden;
  }
  body {
    width: 1200px;
    height: 790px;
    background: var(--backdrop);
    position: relative;
    font-family: "Oswald", sans-serif;
  }
  .sign {
    position: absolute;
    background: var(--sign-white);
    border-radius: 18px;
    box-shadow: 0 2px 6px rgba(0,0,0,0.25);
  }
  .sign__frame {
    position: absolute;
    inset: 8px;
    border: 4px solid var(--brand-teal);
    border-radius: 12px;
    overflow: hidden;
    background: var(--sign-white);
  }
  .sign__band {
    position: absolute;
    background: var(--brand-teal);
  }
  .sign__bottle {
    position: absolute;
    border-radius: 14px 14px 8px 8px;
    background: linear-gradient(180deg, var(--sign-white) 0%, var(--bottle-light) 40%, var(--bottle-mid) 100%);
  }
  .sign__title {
    position: absolute;
    margin: 0;
    color: var(--brand-orange);
    font-weight: 700;
    text-transform: uppercase;
    white-space: nowrap;
  }
  .sign__title span { display: block; }
  .brand-name {
    position: absolute;
    display: flex;
    align-items: center;
    gap: 6px;
    font-family: "Oswald", sans-serif;
    font-weight: 400;
    white-space: nowrap;
  }
  .brand-name__dot {
    display: inline-block;
    border-radius: 50%;
  }

  /* Portrait sign */
  .sign--portrait { left: 70px; top: 90px; width: 431px; height: 609px; }
  .sign--portrait .sign__band { left: 0; top: 0; right: 0; height: 214px; }
  .sign--portrait .sign__bottle { left: 162px; top: 12px; width: 84px; height: 172px; }
  .sign--portrait .sign__title {
    left: 0; right: 0; top: 228px;
    text-align: center;
    font-size: 78px;
    line-height: 77px;
    letter-spacing: -1.5px;
  }
  .sign--portrait .brand-name {
    left: 0; right: 0; top: 520px;
    justify-content: center;
    color: var(--brand-orange);
    font-size: 20px;
  }
  .sign--portrait .brand-name__dot { width: 10px; height: 10px; background: var(--brand-orange); }

  /* Landscape sign */
  .sign--landscape { left: 540px; top: 178px; width: 618px; height: 434px; }
  .sign--landscape .sign__band { left: 0; top: 0; bottom: 0; width: 216px; }
  .sign--landscape .sign__bottle { left: 52px; top: 60px; width: 126px; height: 256px; }
  .sign--landscape .sign__title {
    left: 230px; top: 64px;
    font-size: 86px;
    line-height: 90px;
    letter-spacing: -1px;
  }
  .sign--landscape .brand-name {
    left: 0; width: 216px; top: 360px;
    justify-content: center;
    color: var(--sign-white);
    font-size: 15px;
  }
  .sign--landscape .brand-name__dot { width: 8px; height: 8px; background: var(--sign-white); }
</style>
</head>
<body>

  <section class="sign sign--portrait" aria-label="Hand sanitizer station sign, portrait">
    <div class="sign__frame">
      <div class="sign__band"></div>
      <div class="sign__bottle" role="img" aria-label="Illustration of a pump bottle of hand sanitizer with a medical cross label"></div>
      <h1 class="sign__title"><span>Hand</span><span>Sanitizer</span><span>Station</span></h1>
      <div class="brand-name"><span class="brand-name__dot"></span>Ridge Creek Inn</div>
    </div>
  </section>

  <section class="sign sign--landscape" aria-label="Hand sanitizer station sign, landscape">
    <div class="sign__frame">
      <div class="sign__band"></div>
      <div class="sign__bottle" role="img" aria-label="Illustration of a pump bottle of hand sanitizer with a medical cross label"></div>
      <h2 class="sign__title"><span>Hand</span><span>Sanitizer</span><span>Station</span></h2>
      <div class="brand-name"><span class="brand-name__dot"></span>Ridge Creek Inn</div>
    </div>
  </section>

</body>
</html>
```